2 x storefront vinyl request

We are transitioning to a storefront office and need two vinyls for the windows.

First vinyl: Use the Halloway Partners logo, website (www.hallowaypartnersestates.example) and leasing office number ((555) 314-2786)

Second vinyl: Maintenance Division & phone number (555) 314-2786

```html
<!DOCTYPE html>
<html lang="en">
<head>
<meta charset="utf-8">
<title>Halloway Partners – Storefront Window Vinyls</title>
<link href="https://fonts.googleapis.com/css2?family=Barlow+Condensed:wght@600;700&display=swap" rel="stylesheet">
<style>
  :root {
    --slate: #465563;
    --slate-deep: #3c4a57;
    --mist: #e4e6e9;
    --silver: #c9cdd2;
    --paper: #ffffff;
    --ink: #111111;
    --backdrop: #eef0f2;
  }
  * { box-sizing: border-box; margin: 0; padding: 0; }
  html, body {
    width: 1045px; height: 1200px; overflow: hidden;
    background: var(--backdrop);
    font-family: "Barlow Condensed", "Arial Narrow", sans-serif;
  }
  .window-set { position: relative; width: 1045px; height: 1200px; }
  .vinyl {
    position: absolute; top: 50px; height: 1100px;
    background: var(--paper);
    overflow: hidden;
    box-shadow: 0 4px 18px rgba(0,0,0,0.12);
  }
  .vinyl--leasing { left: 117px; width: 420px; }
  .vinyl--maintenance { left: 617px; width: 310px; }
  .vinyl__backdrop { position: absolute; inset: 0; width: 100%; height: 100%; }
  .brand {
    position: absolute; color: var(--ink); font-weight: 700;
    text-transform: uppercase; line-height: 0.95; letter-spacing: 0.5px;
    white-space: nowrap;
  }
  .vinyl--leasing .brand { left: 90px; top: 250px; font-size: 58px; }
  .vinyl--maintenance .brand { left: 62px; top: 250px; font-size: 44px; }
  .brand__mark {
    display: inline-block; width: 0.45em; height: 0.45em;
    background: var(--slate); margin-left: 8px; vertical-align: middle;
  }
  .message {
    position: absolute; left: 0; right: 0; text-align: center;
    color: var(--slate-deep); font-weight: 700; text-transform: uppercase;
    white-space: nowrap;
  }
  .leasing-label { top: 555px; padding-left: 60px; font-size: 34px; line-height: 1; letter-spacing: 0.3px; }
  .leasing-number { top: 610px; padding-left: 60px; font-size: 84px; line-height: 1; }
  .maintenance-label { top: 520px; padding-left: 40px; font-size: 50px; line-height: 1.15; }
  .footer-band {
    position: absolute; left: 0; right: 0; bottom: 0;
    display: flex; align-items: center; justify-content: center;
    color: var(--paper); font-weight: 600; white-space: nowrap;
  }
  .vinyl--leasing .footer-band { height: 150px; font-size: 24px; padding-left: 20px; }
  .vinyl--maintenance .footer-band { height: 130px; font-size: 38px; font-weight: 700; }
</style>
</head>
<body>
<main class="window-set">

  <section class="vinyl vinyl--leasing" aria-label="Leasing office window vinyl">
    <svg class="vinyl__backdrop" viewBox="0 0 420 1100" preserveAspectRatio="none" aria-hidden="true">
      <path d="M220,20 C330,60 290,420 140,520 C60,600 150,820 420,900 L420,0 L230,0 Z" fill="var(--mist)" opacity="0.55"/>
      <path d="M150,40 C40,120 0,420 10,640 C20,820 70,900 150,950 L0,950 L0,40 Z" fill="var(--slate)"/>
      <path d="M150,40 C60,130 30,420 40,640 C50,820 120,920 230,950 L150,950 C70,900 20,820 10,640 C0,420 40,120 150,40 Z" fill="var(--silver)"/>
      <rect x="0" y="950" width="420" height="150" fill="var(--slate)"/>
    </svg>
    <div class="brand">Halloway<br>Partners<span class="brand__mark"></span></div>
    <p class="message leasing-label">Leasing Office Number</p>
    <p class="message leasing-number">(555)<br>314-2786)</p>
    <p class="footer-band">www.hallowaypartnersestates.example</p>
  </section>

  <section class="vinyl vinyl--maintenance" aria-label="Maintenance division window vinyl">
    <svg class="vinyl__backdrop" viewBox="0 0 310 1100" preserveAspectRatio="none" aria-hidden="true">
      <path d="M170,20 C250,80 220,420 110,520 C50,600 110,820 310,900 L310,0 L180,0 Z" fill="var(--mist)" opacity="0.55"/>
      <path d="M110,40 C30,130 0,420 8,640 C15,820 50,910 110,970 L0,970 L0,40 Z" fill="var(--slate)"/>
      <path d="M110,40 C45,140 25,420 32,640 C40,820 90,930 170,970 L110,970 C50,910 15,820 8,640 C0,420 30,130 110,40 Z" fill="var(--silver)"/>
      <rect x="0" y="970" width="310" height="130" fill="var(--slate)"/>
    </svg>
    <div class="brand">Halloway<br>Partners<span class="brand__mark"></span></div>
    <p class="message maintenance-label">Maintenance<br>Division</p>
    <p class="footer-band">(555) 314-2786</p>
  </section>

</main>
</body>
</html>
```